依頼詳細
近隣のタワーマンションや、ホテル、貸会議室など、中高年層方々向けにチラシを置いてもらう、紹介してもらおうと考えております。シンプル、シックで上品な感じ、尚且つ、目を引く雰囲気にしていただけたらと思います。
記載項目
店名/Lorendal ロレンダール イタリアンダイニングレストラン
電話番号/06-6481-5926
住所:大阪市中央区緑岡町5-4-1 ミネハ紡第三ビル 地下1階
営業時間(Lunch:11:45-14:00、Dinner:17:30~23:30)
ランチメニュー【パスタランチ】¥800~
ディナーメニュー (アンティパスト¥1000~、ピザ.パスタ ¥1400~ お肉、お魚料理 ¥1800~、デザート¥600~)
添付写真イメージ
サイズ
A6
ページ数
両面
希望イメージ
シンプル 複雑
単色 カラフル
暗い 明るい
日常 高級
遊び心 厳粛
未来的 伝統的
女性的 男性的
希望する色
黒、白、ゴールド、木目などの茶色
納品ファイル
• 高解像度JPG (.jpg)
• イラストレーター形式 (.ai)
補足説明
写真や地図などは多少修正して頂いても、使わなくても結構です。
地図は添付の写真を参考にしていただければと思います。
とにかく、わかりやすく、ウリが的確に伝わるようにお願い致します。

```html
<!DOCTYPE html>
<html lang="ja">
<head>
<meta charset="utf-8">
<title>Lorendal イタリアンダイニングレストラン</title>
<link rel="stylesheet" href="https://fonts.googleapis.com/css2?family=Noto+Serif+JP:wght@400;600;700&family=Cormorant+Garamond:wght@500;600&display=swap">
<style>
  :root {
    --night: #0d0805;
    --umber: #2a170c;
    --gold: #d9b25a;
    --gold-pale: #f0d98f;
    --wood-light: #c9a35a;
    --wood-mid: #9c7430;
    --wood-dark: #5e4317;
    --ink: #2b1a08;
    --cream: #f4ecd6;
    --paper: #fff;
  }
  * { margin: 0; padding: 0; box-sizing: border-box; }
  html, body { width: 845px; height: 1200px; overflow: hidden; background: var(--night); }
  .flyer {
    position: relative; width: 845px; height: 1200px; overflow: hidden;
    background: radial-gradient(ellipse at 30% 45%, var(--umber) 0%, var(--night) 70%);
    font-family: "Noto Serif JP", serif; color: var(--paper);
  }
  .interior-photo {
    position: absolute; left: 0; top: 0; width: 592px; height: 335px;
    background: linear-gradient(160deg, #6b3412 0%, #3a1b0a 45%, #1a0c05 100%);
    box-shadow: inset 0 -40px 60px rgba(0,0,0,.6);
  }
  .menu { position: absolute; left: 610px; top: 30px; width: 230px; }
  .menu-heading {
    font-size: 22px; font-weight: 700; letter-spacing: 1px; line-height: 29px; white-space: nowrap;
  }
  .menu-heading::before { content: "◆"; color: var(--gold); font-size: 16px; margin-right: 3px; vertical-align: 2px; }
  .menu-item { font-size: 21px; font-weight: 600; line-height: 26px; padding-left: 22px; white-space: nowrap; }
  .menu-price { font-size: 20px; color: var(--gold-pale); padding-left: 44px; line-height: 26px; margin-bottom: 4px; }
  .menu-lunch { margin-bottom: 18px; }
  .menu-lunch .menu-item { color: var(--gold-pale); }
  .intro {
    position: absolute; left: 252px; top: 368px; width: 330px;
    font-size: 29px; line-height: 42px; color: rgba(255,255,255,.85);
  }
  .dish-photo {
    position: absolute; left: 590px; top: 425px; width: 245px; height: 160px;
    border-radius: 50%;
    background: radial-gradient(ellipse at 50% 45%, #f3ecdf 0%, #d8cbb4 45%, #7a5a35 80%, rgba(13,8,5,0) 100%);
  }
  .hours { position: absolute; left: 600px; top: 605px; width: 235px; text-align: center; }
  .hours-title { font-size: 21px; font-weight: 600; line-height: 30px; }
  .hours-line { font-family: "Cormorant Garamond", serif; font-size: 23px; line-height: 28px; }
  .wood-band {
    position: absolute; left: 0; top: 720px; width: 845px; height: 480px;
    background:
      repeating-linear-gradient(88deg, rgba(255,240,200,.08) 0 6px, rgba(0,0,0,.06) 6px 14px),
      linear-gradient(180deg, var(--wood-mid) 0%, var(--wood-light) 35%, var(--wood-mid) 70%, var(--wood-dark) 100%);
  }
  .wood-band::before {
    content: ""; position: absolute; left: 0; top: 0; width: 100%; height: 100px;
    background: linear-gradient(180deg, var(--night), rgba(13,8,5,0));
  }
  .brand { position: absolute; left: 36px; top: 800px; }
  .brand-type { font-size: 20px; color: var(--cream); letter-spacing: 2px; }
  .brand-row { display: flex; align-items: center; gap: 14px; margin-top: 4px; }
  .brand-name { font-size: 82px; font-weight: 600; color: var(--ink); line-height: 1; letter-spacing: 1px; }
  .brand-mark { width: 18px; height: 18px; background: var(--ink); align-self: flex-start; margin-top: 16px; }
  .brand-kana { font-size: 18px; color: var(--ink); margin-top: 2px; padding-left: 260px; }
  .contact { position: absolute; left: 36px; top: 965px; color: var(--ink); }
  .tel { font-size: 42px; font-weight: 700; color: var(--paper); text-shadow: 0 2px 4px rgba(0,0,0,.45); line-height: 56px; }
  .tel span { font-family: "Cormorant Garamond", serif; font-size: 44px; margin-right: 10px; }
  .address { font-size: 24px; font-weight: 600; line-height: 38px; margin-top: 8px; }
  .access-map {
    position: absolute; left: 538px; top: 790px; width: 300px; height: 395px;
    background: var(--cream); border: 2px solid var(--ink);
  }
</style>
</head>
<body>
<main class="flyer">
  <div class="interior-photo" role="img" aria-label="落ち着いた照明の店内、カウンターとテーブル席の写真"></div>

  <section class="menu">
    <div class="menu-lunch">
      <h2 class="menu-heading">ランチメニュー</h2>
      <p class="menu-item">パスタランチ</p>
      <p class="menu-price">¥800～</p>
    </div>
    <div class="menu-dinner">
      <h2 class="menu-heading">ディナーメニュー</h2>
      <p class="menu-item">アンティパスト</p>
      <p class="menu-price">¥1000～</p>
      <p class="menu-item">ピザ、パスタ</p>
      <p class="menu-price">¥1400～</p>
      <p class="menu-item">お肉、お魚料理</p>
      <p class="menu-price">¥1800～</p>
      <p class="menu-item">デ ザ ー ト</p>
      <p class="menu-price">¥600～</p>
    </div>
  </section>

  <p class="intro">お昼のランチ。<br>ご接待やご商談には<br>個室もご用意。その他<br>各種パーティまで<br>ご利用できます。<br>もちろん くつろぎの<br>空間での会食もご満足<br>いただけます。</p>

  <div class="dish-photo" role="img" aria-label="白い皿に盛られたパスタ料理の写真"></div>

  <section class="hours">
    <h3 class="hours-title">営業時間</h3>
    <p class="hours-line">Lunch/11:45-14:00</p>
    <p class="hours-line">Dinner/17:30～23:30</p>
  </section>

  <div class="wood-band"></div>

  <header class="brand">
    <p class="brand-type">イタリアン ダイニングレストラン</p>
    <div class="brand-row">
      <span class="brand-name">Lorendal</span>
      <span class="brand-mark"></span>
    </div>
    <p class="brand-kana">ロレンダール</p>
  </header>

  <section class="contact">
    <p class="tel"><span>tel</span>06-6481-5926</p>
    <p class="address">大阪市中央区緑岡町5-4-1<br>ミネハ紡第三ビル地下1階</p>
  </section>

  <div class="access-map" role="img" aria-label="最寄り駅から店舗までのアクセス地図"></div>
</main>
</body>
</html>
```